Studying Effectively To Do List

I am looking to design a new "Study To Do List" for High School students (Ages 15 - 18) . This will be printed as an A4 notepad and so should only be a single A4 page.

The Design will need to be professional and look semi-serious but also be appealing to High school students (Ages 15 - 18) and should NOT be gender specific.

I have attached a word document outlining the structure of the page. The space provided should be large enough that people can write in it comfortably.

The notepad will most likely be printed in black and white but I'm also looking at coloured options - colours should be kept to a minimum.

This will be printed professionally and should also include a 3mm bleed.

The design should also include the business logo (included in the word document)

Target Market(s)

High School students (Ages 15 - 18). Both genders

Industry/Entity Type

Education

Font styles to use
Serif
Sans Serif

Requirements
Must have
• Please see the word document attached.
Should not have
• Too much colour

```html
<!DOCTYPE html>
<html lang="en">
<head>
<meta charset="utf-8">
<title>Study To Do List</title>
<link href="https://fonts.googleapis.com/css2?family=Open+Sans:wght@400;600;700&display=swap" rel="stylesheet">
<style>
  :root {
    --orange: #f7760b;
    --charcoal: #3d3d3f;
    --ink: #2b2b2b;
    --navy: #1f3347;
    --rule: #555;
    --paper: #ffffff;
    --paper-shade: #f1f1f1;
    --backdrop: #e7e4df;
  }
  * { box-sizing: border-box; margin: 0; padding: 0; }
  html, body { width: 1020px; height: 1200px; overflow: hidden; }
  body {
    background: var(--backdrop);
    font-family: "Open Sans", Arial, sans-serif;
    color: var(--ink);
    position: relative;
  }
  .sheet {
    position: absolute;
    left: 90px; top: 6px;
    width: 840px; height: 1188px;
    background: linear-gradient(160deg, var(--paper) 0%, var(--paper-shade) 55%, var(--paper) 100%);
    overflow: hidden;
  }
  .header-wave { position: absolute; left: 0; top: 0; width: 840px; height: 160px; }
  .brand-disc {
    position: absolute; left: 33px; top: 14px;
    width: 184px; height: 184px; border-radius: 50%;
    background: var(--paper);
    display: flex; align-items: center; justify-content: center;
    box-shadow: 0 1px 4px rgba(0,0,0,.15);
  }
  .brand-name { font-weight: 700; font-size: 30px; color: var(--navy); letter-spacing: .5px; }
  .website {
    position: absolute; left: 545px; top: 32px;
    display: flex; align-items: center; gap: 10px;
    color: #fff; font-size: 22px;
  }
  .section-tag {
    position: absolute; left: 358px;
    width: 121px; height: 34px; border-radius: 5px;
    background: var(--orange);
    color: #fff; font-weight: 700; font-size: 14px;
    display: flex; align-items: center; justify-content: center;
    box-shadow: 0 3px 3px rgba(0,0,0,.22);
  }
  .section-tag.wide { left: 352px; width: 133px; }
  .date-field {
    position: absolute; left: 602px; top: 166px;
    display: flex; align-items: flex-end; font-size: 16px;
  }
  .date-field .line { display: block; width: 178px; border-bottom: 1.3px solid var(--rule); margin-left: 2px; height: 18px; }
  .grid {
    position: absolute; left: 18px; width: 799px;
    border-collapse: collapse; font-size: 14px;
  }
  .grid td, .grid th { border: 1.3px solid var(--rule); padding: 0 12px; height: 27px; text-align: left; font-weight: 400; }
  .grid th { text-align: center; font-weight: 700; height: 28px; }
  .grid th.small { font-size: 13px; }
  .revision { top: 218px; }
  .notes { top: 1013px; }
  .lines { position: absolute; left: 18px; width: 799px; }
  .write-row { display: flex; align-items: flex-end; height: 22.2px; font-size: 14px; }
  .write-row .fill { flex: 1; border-bottom: 1.3px solid var(--rule); margin-left: 3px; margin-bottom: 4px; }
  .homework { top: 389px; }
  .assessments { top: 707px; }
  .assessments .write-row { height: 23.2px; }
  .write-row .fill.short { flex: none; width: 297px; }
  .write-row .due { margin-left: 8px; }
  .write-row .fill.end { margin-right: 4px; }
  .foot-bar { position: absolute; left: 0; bottom: 3px; width: 840px; height: 10px; display: flex; }
  .foot-bar .left { width: 418px; background: var(--orange); }
  .foot-bar .right { flex: 1; background: var(--charcoal); }
</style>
</head>
<body>
<div class="sheet">
  <svg class="header-wave" viewBox="0 0 840 160" aria-hidden="true">
    <path d="M0 88 C80 68 160 52 250 62 C350 74 420 134 520 138 C640 142 760 132 840 98 L840 104 C760 142 640 152 520 150 C420 148 340 90 250 80 C160 70 80 90 0 122 Z" fill="#3d3d3f"/>
    <path d="M0 0 H840 V96 C760 130 640 140 520 136 C420 132 350 72 250 60 C160 50 80 66 0 86 Z" fill="#f7760b"/>
  </svg>

  <div class="brand-disc"><span class="brand-name">Keystone</span></div>

  <div class="website">
    <svg width="22" height="22" viewBox="0 0 24 24" fill="none" stroke="#fff" stroke-width="1.8" aria-hidden="true">
      <circle cx="12" cy="12" r="10"/><ellipse cx="12" cy="12" rx="4.5" ry="10"/><line x1="2" y1="12" x2="22" y2="12"/>
    </svg>
    <span>www.yourwebsite.com</span>
  </div>

  <div class="section-tag" style="top:160px">REVISION</div>
  <div class="date-field">Date:<span class="line"></span></div>

  <table class="grid revision">
    <tr><td style="width:400px">1</td><td>5</td></tr>
    <tr><td>2</td><td>6</td></tr>
    <tr><td>3</td><td>7</td></tr>
    <tr><td>4</td><td>8</td></tr>
  </table>

  <div class="section-tag" style="top:345px">HOMEWORK</div>
  <div class="lines homework">
    <div class="write-row">Subject:<span class="fill"></span></div>
    <div class="write-row">Task:<span class="fill"></span></div>
    <div class="write-row">Subject:<span class="fill"></span></div>
    <div class="write-row">Task:<span class="fill"></span></div>
    <div class="write-row">Subject:<span class="fill"></span></div>
    <div class="write-row">Task:<span class="fill"></span></div>
    <div class="write-row">Subject:<span class="fill"></span></div>
    <div class="write-row">Task:<span class="fill"></span></div>
    <div class="write-row">Subject:<span class="fill"></span></div>
    <div class="write-row">Task:<span class="fill"></span></div>
    <div class="write-row">Subject:<span class="fill"></span></div>
    <div class="write-row">Task:<span class="fill"></span></div>
  </div>

  <div class="section-tag wide" style="top:661px">ASSESSMENTS</div>
  <div class="lines assessments">
    <div class="write-row">Assessment:<span class="fill short"></span><span class="due">Due</span><span class="fill"></span></div>
    <div class="write-row">Element:<span class="fill end"></span></div>
    <div class="write-row">Assessment:<span class="fill short"></span><span class="due">Due</span><span class="fill"></span></div>
    <div class="write-row">Element:<span class="fill end"></span></div>
    <div class="write-row">Assessment:<span class="fill short"></span><span class="due">Due</span><span class="fill"></span></div>
    <div class="write-row">Element:<span class="fill end"></span></div>
    <div class="write-row">Assessment:<span class="fill short"></span><span class="due">Due</span><span class="fill"></span></div>
    <div class="write-row">Element:<span class="fill end"></span></div>
    <div class="write-row">Assessment:<span class="fill short"></span><span class="due">Due</span><span class="fill"></span></div>
    <div class="write-row">Element:<span class="fill end"></span></div>
    <div class="write-row">Assessment:<span class="fill short"></span><span class="due">Due</span><span class="fill"></span></div>
    <div class="write-row">Element:<span class="fill end"></span></div>
  </div>

  <table class="grid notes">
    <tr><th colspan="2">NOTES</th><th class="small">PRACTICE</th></tr>
    <tr><td style="width:200px">1</td><td style="width:200px"></td><td>5</td></tr>
    <tr><td>2</td><td></td><td>6</td></tr>
    <tr><td>3</td><td></td><td>7</td></tr>
    <tr><td>4</td><td></td><td>8</td></tr>
  </table>

  <div class="foot-bar"><span class="left"></span><span class="right"></span></div>
</div>
</body>
</html>
```